Harvest Gathering event flyer

I would like a church event flyer designed. The event is called "HARVEST GATHERING 2018". I am looking for a professional, yet catchy design that uses our brand colors and logo creatively while communicating key information of the event effectively.

1. The logo is attached in two color formats. The designer has the choice to use them as he/she want.

2. The location of the event is: Lindqvist Community Center, 482 Tamsworth Street, Portland, ME 04102
3. Time and date of event. The designer can organize and format the date and time as he/she pleases.
December 28th, 29th @ 7:00PM
December 30th @ 10:00AM
4. The topic of the event is "Tongues of fire". The designer is free to use this phrase as he/she pleases to create a good composition.
5. Speaker: Prophet Marcus Obuya
6. Contact information: contact@cedarbrookfellowship.org - Telephone number: 207 555 0148

7. I would also like the following three words on the flyer. These words describe the focus of the event: FIRE, REVIVAL, PROPHETIC

```html
<!DOCTYPE html>
<html lang="en">
<head>
<meta charset="utf-8">
<title>Harvest Gathering 2018 – Flyer</title>
<link rel="stylesheet" href="https://fonts.googleapis.com/css2?family=Cinzel:wght@400;600;700;900&display=swap">
<style>
  :root {
    --page: #ecebe8;
    --navy: #0d355b;
    --navy-deep: #0a2c4d;
    --orange: #f4941f;
    --orange-light: #f7a534;
    --orange-dark: #e7871a;
    --white: #ffffff;
    --photo-top: #e0b540;
    --photo-mid: #a8672a;
    --photo-low: #5a3318;
  }
  * { margin: 0; padding: 0; box-sizing: border-box; }
  html, body {
    width: 1200px; height: 1200px; overflow: hidden;
    background: var(--page);
  }
  .flyer {
    position: absolute; left: 190px; top: 20px;
    width: 820px; height: 1160px;
    background: var(--navy);
    overflow: hidden;
    font-family: "Cinzel", serif;
    color: var(--white);
  }
  .flyer-shapes { position: absolute; inset: 0; }
  .text-block { position: absolute; left: 0; width: 100%; text-align: center; white-space: nowrap; }
  .event-title { top: 96px; font-size: 50px; font-weight: 700; letter-spacing: 1px; line-height: 1; }
  .event-year { top: 152px; font-size: 70px; font-weight: 700; line-height: 1; }
  .brand-name {
    position: absolute; left: 78px; top: 518px;
    font-size: 66px; font-weight: 400; line-height: 1; color: var(--white);
  }
  .topic { top: 646px; font-size: 58px; font-weight: 600; color: var(--orange); letter-spacing: 1px; line-height: 1; }
  .focus-words { top: 706px; font-size: 24px; font-weight: 600; letter-spacing: 1px; }
  .focus-words .sep { margin: 0 14px; font-weight: 400; }
  .schedule { font-size: 36px; font-weight: 600; line-height: 1; }
  .schedule sup { font-size: 18px; vertical-align: 16px; }
  .schedule-evening { top: 762px; }
  .schedule-morning { top: 819px; }
  .schedule-rule { position: absolute; left: 95px; top: 806px; width: 616px; height: 1px; background: var(--white); }
  .speaker {
    position: absolute; left: 243px; top: 882px; width: 333px; height: 59px;
    border: 1.5px solid var(--orange); text-align: center;
  }
  .speaker-label { height: 22px; background: var(--orange); font-size: 19px; font-weight: 600; line-height: 22px; }
  .speaker-name { font-size: 22px; font-weight: 600; line-height: 34px; }
  .venue { top: 966px; font-size: 19px; font-weight: 600; line-height: 25px; }
  .contact-rule { position: absolute; left: 248px; top: 1054px; width: 317px; height: 1px; background: var(--white); }
  .contact-label { top: 1064px; font-size: 19px; font-weight: 600; color: var(--orange); }
  .contact-line { top: 1089px; font-size: 17px; font-weight: 600; }
  .contact-line .sep { margin: 0 14px; }
</style>
</head>
<body>
  <main class="flyer">
    <svg class="flyer-shapes" width="820" height="1160" viewBox="0 0 820 1160">
      <defs>
        <linearGradient id="nave" x1="0" y1="0" x2="0" y2="1">
          <stop offset="0" stop-color="var(--photo-mid)"/>
          <stop offset="0.3" stop-color="var(--photo-top)"/>
          <stop offset="0.75" stop-color="var(--photo-mid)"/>
          <stop offset="1" stop-color="var(--photo-low)"/>
        </linearGradient>
      </defs>
      <g role="img" aria-label="Photograph of a gothic cathedral nave with vaulted ceiling and arches">
        <polygon points="0,0 820,0 820,689 0,318" fill="url(#nave)"/>
      </g>
      <polygon points="0,318 820,689 820,699 0,328" fill="var(--orange)"/>
      <polygon points="820,318 820,689 526,556" fill="var(--orange)"/>
      <polygon points="820,318 820,470 700,560 526,556" fill="var(--orange-light)"/>
      <polygon points="700,560 820,689 820,470" fill="var(--orange-dark)" opacity="0.5"/>
    </svg>

    <h1 class="text-block event-title">Harvest Gathering</h1>
    <p class="text-block event-year">2018</p>

    <p class="brand-name">KALDEN</p>

    <h2 class="text-block topic">Tongues of Fire</h2>
    <p class="text-block focus-words">Fire<span class="sep">|</span>Revival<span class="sep">|</span>Prophetic</p>

    <p class="text-block schedule schedule-evening">December 28<sup>th</sup>, 29<sup>th</sup> @ 7:00PM</p>
    <div class="schedule-rule"></div>
    <p class="text-block schedule schedule-morning">December 30<sup>th</sup> @ 10:00AM</p>

    <div class="speaker">
      <div class="speaker-label">Speaker:</div>
      <div class="speaker-name">Prophet Marcus Obuya</div>
    </div>

    <p class="text-block venue">Lindqvist Community Center,<br>482 Tamsworth Street, Portland, ME 04102</p>

    <div class="contact-rule"></div>
    <p class="text-block contact-label">Contact information:</p>
    <p class="text-block contact-line">contact@cedarbrookfellowship.org<span class="sep">|</span>Tel No: 207 555 0148</p>
  </main>
</body>
</html>
```